Business Card Re-Design for a Lighting Designer

I would like my business card re-designed. It is currently high gloss and they scratch too easily. I don not think the current design lends itself well to a matte finish. I have included the current design for reference along with our company logo.
Check out our website for current branding.
http://www.brambleorchidstudio.example

Updates
Some of the top contenders are muslim and it is a holiday for them. I do not want to discriminate and would expect the same courtesy for holidays we celebrate.
Target Market(s)
Interior Designers, Architects
Contact Information for Business Card
Logo - Name, Title, Address, Telephone Number and Extension, Email
Font styles to use
Requirements
Must have
- All the information listed on the current business card. If you use Red, it needs to be the red from our logo.
Nice to have
- Vertical and Horizontal Designs will be entertained.
Should not have
- Requirements for a glossy finish...should not look too corporate since we are a design firm.

```html
<!DOCTYPE html>
<html lang="en">
<head>
<meta charset="utf-8">
<title>Bramble Orchid Studio — Business Card</title>
<link href="https://fonts.googleapis.com/css2?family=Lato:wght@400;700&family=Oswald:wght@600&display=swap" rel="stylesheet">
<style>
  :root {
    --backdrop: #141414;
    --card: #262626;
    --card-light: #2e2e2e;
    --brand-red: #a3262a;
    --ink: #f2f2f2;
    --ink-muted: #c9c9c9;
  }
  * { box-sizing: border-box; margin: 0; padding: 0; }
  html, body { width: 1200px; height: 900px; overflow: hidden; }
  body {
    background: var(--backdrop);
    font-family: "Lato", sans-serif;
    color: var(--ink);
    position: relative;
  }
  .card {
    position: absolute;
    left: 280px;
    width: 640px;
    height: 366px;
    background: linear-gradient(135deg, var(--card) 0%, var(--card) 55%, var(--card-light) 100%);
    border-bottom: 5px solid var(--brand-red);
    box-shadow: 0 18px 40px rgba(0,0,0,0.55);
  }
  .card--front { top: 60px; }
  .card--back { top: 474px; }

  /* Front */
  .brand {
    position: absolute;
    left: 50%;
    top: 50%;
    transform: translate(-50%, -50%);
    display: flex;
    align-items: center;
    gap: 18px;
  }
  .brand__square {
    width: 58px;
    height: 58px;
    background: var(--brand-red);
  }
  .brand__name {
    font-size: 30px;
    font-weight: 400;
    letter-spacing: 2px;
    line-height: 1.15;
    color: var(--ink);
    text-transform: uppercase;
  }

  /* Back */
  .identity {
    position: absolute;
    right: 368px;
    top: 118px;
    text-align: right;
  }
  .identity__name {
    font-family: "Oswald", sans-serif;
    font-weight: 600;
    font-size: 40px;
    letter-spacing: 1px;
    color: var(--brand-red);
    line-height: 1;
    text-transform: uppercase;
  }
  .identity__title {
    font-size: 17px;
    letter-spacing: 1px;
    color: var(--ink);
    margin-top: 6px;
    text-transform: uppercase;
  }
  .divider {
    position: absolute;
    left: 290px;
    top: 116px;
    width: 2px;
    height: 70px;
    background: var(--brand-red);
  }
  .contacts {
    position: absolute;
    left: 314px;
    top: 112px;
    list-style: none;
  }
  .contacts__item {
    display: flex;
    align-items: center;
    gap: 10px;
    font-size: 17px;
    line-height: 26px;
    color: var(--ink);
  }
  .contacts__icon { width: 13px; height: 13px; flex: none; }
  .address {
    position: absolute;
    left: 0;
    right: 0;
    bottom: 40px;
    text-align: center;
    font-size: 18px;
    color: var(--ink);
  }
</style>
</head>
<body>
  <section class="card card--front">
    <div class="brand">
      <span class="brand__square"></span>
      <span class="brand__name">Bramble Orchid<br>Studio</span>
    </div>
  </section>

  <section class="card card--back">
    <div class="identity">
      <p class="identity__name">Maren Holloway</p>
      <p class="identity__title">Principal</p>
    </div>
    <span class="divider"></span>
    <ul class="contacts">
      <li class="contacts__item">
        <svg class="contacts__icon" viewBox="0 0 16 16"><path fill="#a3262a" d="M4 1l2.5 3-1.5 2c1 2 3 4 5 5l2-1.5 3 2.5-1.5 2.5C8 15 1 8 1.5 2.5z"/></svg>
        555.014.2290 x1
      </li>
      <li class="contacts__item">
        <svg class="contacts__icon" viewBox="0 0 16 16"><rect x="1" y="3" width="14" height="10" fill="none" stroke="#a3262a" stroke-width="1.5"/><path d="M1 3l7 6 7-6" fill="none" stroke="#a3262a" stroke-width="1.5"/></svg>
        maren@brambleorchidstudio.example
      </li>
      <li class="contacts__item">
        <svg class="contacts__icon" viewBox="0 0 16 16"><circle cx="8" cy="8" r="6.5" fill="none" stroke="#a3262a" stroke-width="1.4"/><ellipse cx="8" cy="8" rx="3" ry="6.5" fill="none" stroke="#a3262a" stroke-width="1.2"/><path d="M1.5 8h13" stroke="#a3262a" stroke-width="1.2"/></svg>
        www.brambleorchidstudio.example
      </li>
    </ul>
    <p class="address">218 Larkfield Commons Suite 40 Marlow, Georgia 30999</p>
  </section>
</body>
</html>
```